Cedarfield Supply METAL business card

A metal business card design. Attached are older designs for a reference, but we want a NEW design, not the same as in the past. See the 2 examples just posted. We would like some cut out in the design. Possibly the pine cone or the pine tree branch (see image IMG_0).

Target Market(s)

Home and Gardern

Industry/Entity Type

Landscape

Contact Information for Business Card

Logo, website, address, name, phone numbers

```html
<!DOCTYPE html>
<html lang="en">
<head>
<meta charset="utf-8">
<title>Cedarfield Supply – Metal Business Card</title>
<link rel="stylesheet" href="https://fonts.googleapis.com/css2?family=Cabin:wght@400;600;700&display=swap">
<style>
  :root {
    --bg: #e9e6e1;
    --card: #161616;
    --card-edge: #232323;
    --accent: #c8622a;
    --text: #d9d9d9;
    --name: #a9a9a9;
    --emboss: #222222;
  }
  * { box-sizing: border-box; margin: 0; padding: 0; }
  html, body {
    width: 1200px; height: 900px; overflow: hidden;
    background: var(--bg);
    font-family: "Cabin", sans-serif;
  }
  .canvas { position: relative; width: 1200px; height: 900px; }

  .card {
    position: absolute;
    width: 700px; height: 400px;
    background: var(--card);
    border-radius: 44px;
    box-shadow: 0 10px 28px rgba(0,0,0,.25);
    overflow: hidden;
  }
  .card--front { left: 110px; top: 35px; }
  .card--back  { left: 390px; top: 465px; }

  .needle-cluster {
    position: absolute;
    width: 380px; height: 300px;
    border-radius: 50%;
    background: radial-gradient(circle at 50% 50%, #262626 0%, #1f1f1f 30%, #1b1b1b 60%, rgba(22,22,22,0) 72%);
  }
  .card--front .needle-cluster { left: 80px; top: 150px; }
  .card--back .needle-cluster  { left: 370px; top: 20px; }

  .brand {
    position: absolute;
    display: flex; align-items: center; gap: 12px;
    color: var(--accent);
    font-weight: 700;
    white-space: nowrap;
  }
  .brand__dot {
    width: 20px; height: 20px; border-radius: 50%;
    background: var(--accent);
    flex: none;
  }
  .card--front .brand { left: 340px; top: 85px; font-size: 38px; }
  .card--back .brand  { left: 45px; top: 95px; font-size: 30px; }

  .contact { position: absolute; left: 120px; top: 200px; color: var(--text); }
  .contact__name {
    font-size: 22px; font-weight: 700; letter-spacing: 2px;
    color: var(--name); text-transform: uppercase;
    margin-bottom: 16px;
  }
  .contact__list { list-style: none; font-size: 17px; }
  .contact__item { display: flex; align-items: center; gap: 12px; margin-bottom: 8px; }
  .contact__icon { width: 18px; height: 18px; flex: none; }

  .divider {
    position: absolute; left: 150px; top: 320px;
    width: 340px; height: 2px; background: var(--accent);
  }
  .address {
    position: absolute; left: 160px; top: 335px;
    font-size: 17px; color: var(--text); letter-spacing: .3px;
  }
</style>
</head>
<body>
<main class="canvas">

  <section class="card card--front" aria-label="Card front">
    <div class="needle-cluster" role="img" aria-label="Embossed pine needle cluster cut-out"></div>
    <div class="brand"><span class="brand__dot"></span>Cedarfield Supply</div>
  </section>

  <section class="card card--back" aria-label="Card back">
    <div class="needle-cluster" role="img" aria-label="Embossed pine needle cluster cut-out"></div>
    <div class="brand"><span class="brand__dot"></span>Cedarfield Supply</div>

    <div class="contact">
      <p class="contact__name">Dalton Reeves</p>
      <ul class="contact__list">
        <li class="contact__item">
          <svg class="contact__icon" viewBox="0 0 24 24" fill="none" stroke="currentColor" stroke-width="2" stroke-linecap="round" stroke-linejoin="round"><path d="M22 16.9v3a2 2 0 0 1-2.2 2 19.8 19.8 0 0 1-8.6-3.1 19.5 19.5 0 0 1-6-6A19.8 19.8 0 0 1 2.1 4.2 2 2 0 0 1 4.1 2h3a2 2 0 0 1 2 1.7c.1 1 .4 1.9.7 2.8a2 2 0 0 1-.5 2.1L8 9.9a16 16 0 0 0 6 6l1.3-1.3a2 2 0 0 1 2.1-.4c.9.3 1.8.6 2.8.7a2 2 0 0 1 1.7 2z"/></svg>
          888-555-0142
        </li>
        <li class="contact__item">
          <svg class="contact__icon" viewBox="0 0 24 24" fill="none" stroke="currentColor" stroke-width="2" stroke-linecap="round" stroke-linejoin="round"><path d="M22 16.9v3a2 2 0 0 1-2.2 2 19.8 19.8 0 0 1-8.6-3.1 19.5 19.5 0 0 1-6-6A19.8 19.8 0 0 1 2.1 4.2 2 2 0 0 1 4.1 2h3a2 2 0 0 1 2 1.7c.1 1 .4 1.9.7 2.8a2 2 0 0 1-.5 2.1L8 9.9a16 16 0 0 0 6 6l1.3-1.3a2 2 0 0 1 2.1-.4c.9.3 1.8.6 2.8.7a2 2 0 0 1 1.7 2z"/></svg>
          601-555-0187
        </li>
        <li class="contact__item">
          <svg class="contact__icon" viewBox="0 0 24 24" fill="none" stroke="currentColor" stroke-width="2"><circle cx="12" cy="12" r="10"/><path d="M2 12h20M12 2a15 15 0 0 1 0 20M12 2a15 15 0 0 0 0 20"/></svg>
          cedarfieldsupply.com
        </li>
      </ul>
    </div>

    <div class="divider"></div>
    <p class="address">240 Harlow Ridge Rd, Brandon, MS 39047, USA</p>
  </section>

</main>
</body>
</html>
```